Stationary (letterhead, envelopes, business cards and e-mail signature) for law firm
Law Office of Warren T. Felding
Creative Brief
Professional
Warren T. Felding
Attorney at Law
41 Linden Court, Suite 500 Irvine, California 92731
wfelding@lawwtf-example.com
www.lawwtf-example.com
I would also like my direct dial phone number to appear on the card (in addition to my main number. The Direct number is (714) 555-0187
I would like my logo and maybe my website address to appear on the back. Please be creative.

```html
<!DOCTYPE html>
<html lang="en">
<head>
<meta charset="utf-8">
<title>Law Office of Warren T. Felding — Business Card</title>
<link rel="stylesheet" href="https://fonts.googleapis.com/css2?family=Cinzel:wght@400;500&family=Cormorant+Garamond:wght@400;500;600&display=swap">
<style>
  :root {
    --navy: #1f2a5c;
    --ink: #2b2f3a;
    --muted: #6b6f7a;
    --paper: #ffffff;
    --backdrop: #eceef2;
    --rule: #c9ccd4;
  }
  * { box-sizing: border-box; margin: 0; padding: 0; }
  html, body { width: 1200px; height: 629px; overflow: hidden; background: var(--backdrop); }
  .stage {
    width: 1200px; height: 629px;
    display: flex; align-items: center; justify-content: center; gap: 60px;
  }
  .card {
    position: relative;
    width: 510px; height: 292px;
    background: var(--paper);
    box-shadow: 0 6px 20px rgba(20, 28, 60, 0.14);
    overflow: hidden;
  }
  .firm-mark { display: flex; align-items: center; gap: 12px; }
  .firm-mark__square { width: 12px; height: 12px; background: var(--navy); flex: none; }
  .firm-mark__name {
    font-family: "Cinzel", serif; font-weight: 400;
    color: var(--navy); text-transform: uppercase; line-height: 1.25;
  }
  .firm-mark__name small { display: block; font-size: 0.62em; letter-spacing: 0.28em; }
  .firm-mark__name span { display: block; letter-spacing: 0.08em; }

  /* Back */
  .card--back { display: flex; flex-direction: column; align-items: center; justify-content: center; }
  .card--back .firm-mark__name { font-size: 22px; }
  .card--back .web {
    margin-top: 20px;
    font-family: "Cormorant Garamond", serif; font-weight: 500;
    font-size: 12px; letter-spacing: 0.32em; color: var(--muted); text-transform: uppercase;
  }

  /* Front */
  .card--front .firm-mark { position: absolute; left: 28px; top: 74px; }
  .card--front .firm-mark__name { font-size: 15px; }
  .attorney { position: absolute; left: 28px; top: 166px; font-family: "Cormorant Garamond", serif; }
  .attorney__name { font-size: 16px; font-weight: 600; color: var(--navy); letter-spacing: 0.06em; font-variant: small-caps; }
  .attorney__title { font-size: 11px; color: var(--muted); letter-spacing: 0.08em; font-style: italic; }
  .attorney__mail { margin-top: 16px; font-size: 11px; color: var(--muted); letter-spacing: 0.04em; }
  .contacts {
    position: absolute; left: 262px; top: 56px;
    list-style: none; font-family: "Cormorant Garamond", serif;
    font-size: 12.5px; color: var(--ink); border-left: 1px solid var(--rule); padding-left: 16px;
  }
  .contacts li { display: flex; align-items: center; gap: 9px; height: 26px; }
  .contacts .icon { width: 16px; height: 16px; flex: none; }
  .contacts .icon circle { fill: var(--navy); }
  .contacts .icon path { fill: none; stroke: #fff; stroke-width: 1.2; stroke-linecap: round; stroke-linejoin: round; }
  .band {
    position: absolute; left: 0; right: 0; bottom: 0; height: 32px;
    background: var(--navy); display: flex; align-items: center; justify-content: flex-end; padding-right: 28px;
    font-family: "Cormorant Garamond", serif; font-size: 12px; letter-spacing: 0.3em; color: #fff; text-transform: uppercase;
  }
</style>
</head>
<body>
<main class="stage">
  <section class="card card--back" aria-label="Card back">
    <div class="firm-mark">
      <div class="firm-mark__square"></div>
      <div class="firm-mark__name"><small>Law Office of</small><span>Warren T. Felding</span></div>
    </div>
    <p class="web">www.lawwtf-example.com</p>
  </section>

  <section class="card card--front" aria-label="Card front">
    <div class="firm-mark">
      <div class="firm-mark__square"></div>
      <div class="firm-mark__name"><small>Law Office of</small><span>Warren T. Felding</span></div>
    </div>
    <div class="attorney">
      <p class="attorney__name">Warren T. Felding</p>
      <p class="attorney__title">Attorney at Law</p>
      <p class="attorney__mail">wfelding@lawwtf-example.com</p>
    </div>
    <ul class="contacts">
      <li><svg class="icon" viewBox="0 0 16 16"><circle cx="8" cy="8" r="8"/><path d="M8 12.2s-3-3.2-3-5.2a3 3 0 0 1 6 0c0 2-3 5.2-3 5.2z"/></svg>41 Linden Court, Suite 500</li>
      <li><svg class="icon" viewBox="0 0 16 16"><circle cx="8" cy="8" r="8"/><path d="M5 8h6"/></svg>Irvine, California 92731</li>
      <li><svg class="icon" viewBox="0 0 16 16"><circle cx="8" cy="8" r="8"/><path d="M5.5 4.5l1.5 0 .8 2-1 .8a5 5 0 0 0 1.9 1.9l.8-1 2 .8v1.5a1 1 0 0 1-1 1A6 6 0 0 1 4.5 5.5a1 1 0 0 1 1-1z"/></svg>Direct (714) 555-0187</li>
      <li><svg class="icon" viewBox="0 0 16 16"><circle cx="8" cy="8" r="8"/><path d="M5.5 4.5l1.5 0 .8 2-1 .8a5 5 0 0 0 1.9 1.9l.8-1 2 .8v1.5a1 1 0 0 1-1 1A6 6 0 0 1 4.5 5.5a1 1 0 0 1 1-1z"/></svg>Main (714) 555-0160</li>
      <li><svg class="icon" viewBox="0 0 16 16"><circle cx="8" cy="8" r="8"/><path d="M4.5 5.5h7v5h-7zM4.5 5.5l3.5 2.7 3.5-2.7"/></svg>wfelding@lawwtf-example.com</li>
    </ul>
    <div class="band">www.lawwtf-example.com</div>
  </section>
</main>
</body>
</html>
```